Web Design Project (Mente Lumo)

We are going to do a therapy template to a psychologist. The site already exists, adress: www.mentelumo.net. So, its a total redesign job. I'm from Brazil, the language is PT-BR, so I'm gonna translate what you think be necessary. You can use the current structure from the website as a base to the new design. Check this template to see what I usually like: http://www.layoutkiosk.example/demo/51937.html
Updates

I'm waiting for new creative designs. The 'structure' image is just for 'pb'.

Requirements
Must have
• We need a modern menu, it should use a cool font style and make some kind of effect and little noise when the user pass over with the mouse (FLASH/HTML 5). The main page must emphasize the fact that we offer online treatment, like a picture or frame saying "Online Treatment, click here". It must also show the therapist picture and her name. The colors need to pass a tranquility feeling. The clinic telephone must always be present, doesn't matter which page the user is. The website must adapt to any resolution above 1024x768, crossbrowsing and accept javascript (I'll use www.agendrix.example, so its necessary embed code)
Nice to have
• I would appreciate if there was some kind of slow background animation, passing behind the text using the transparency.
Should not have
• Can't take too long to load, and won't have news or blog

```html
<!DOCTYPE html>
<html lang="pt-BR">
<head>
<meta charset="utf-8">
<title>Mente Lumo – Localização</title>
<link href="https://fonts.googleapis.com/css2?family=Ubuntu:ital,wght@0,300;0,400;0,500;0,700;1,300;1,400;1,700&family=Oswald:wght@400&display=swap" rel="stylesheet">
<style>
:root{
  --nav-dark:#2a6d8c;
  --nav:#4aa3c2;
  --nav-light:#7cc3d9;
  --teal:#1f9c93;
  --teal-light:#3cbcb0;
  --hero-bg:#e6f1f4;
  --cream:#f4f6ea;
  --text:#3b3b3b;
  --heading:#1f2a33;
  --title-blue:#2e5a78;
  --field:#eeeee8;
  --field-border:#dcdcd4;
  --accent-red:#c0392b;
  --footer:#5bb3cb;
  --pink:#b8578a;
  --blue-btn:#1d5f86;
}
*{box-sizing:border-box;margin:0;padding:0}
html,body{width:976px;height:1200px;overflow:hidden}
body{position:relative;background:var(--cream);font-family:"Ubuntu",sans-serif;color:var(--text)}
.abs{position:absolute}

/* header */
.topband{left:0;top:0;width:976px;height:30px;background:linear-gradient(#2f6f8f,#3b86a6)}
.navbar{left:0;top:30px;width:976px;height:42px;background:linear-gradient(var(--nav-light),var(--nav));box-shadow:0 2px 4px rgba(0,0,0,.15)}
.nav a{position:absolute;top:46px;color:#fff;font-size:11px;font-weight:500;text-decoration:none;white-space:nowrap;text-shadow:0 1px 1px rgba(0,0,0,.3);z-index:3}
.nav .dot{position:absolute;top:51px;width:4px;height:4px;border-radius:50%;background:#dff2f7;z-index:3}
.ribbon{left:681px;top:0;width:88px;height:90px;background:var(--teal);z-index:2}
.ribbon::after{content:"";position:absolute;left:4px;right:4px;top:0;bottom:4px;border:1px dashed rgba(255,255,255,.6);border-top:0}
.logo{left:383px;top:5px;width:196px;height:87px;background:linear-gradient(#eaf7fa,#c6e6ee);border:3px solid #bfe0e9;border-radius:30px 30px 40px 40px;display:flex;align-items:center;justify-content:center;gap:8px;z-index:4;box-shadow:0 3px 6px rgba(0,0,0,.15)}
.logo .mark{width:12px;height:12px;border-radius:50%;background:var(--teal)}
.logo .name{font-family:"Ubuntu",sans-serif;font-weight:500;font-size:22px;color:var(--teal)}

/* hero */
.hero{left:0;top:72px;width:976px;height:343px;background:linear-gradient(180deg,#dcecf1,var(--hero-bg) 40%,#eef6f7);border-bottom:1px solid #cfe2d8}
.hero-kicker{left:177px;top:146px;font-size:20px;font-weight:300;font-style:italic;color:var(--title-blue)}
.hero-title{left:243px;top:174px;font-size:23px;font-weight:700;font-style:italic;color:var(--heading)}
.hero-text{left:164px;top:221px;width:310px;font-size:10.5px;font-weight:300;line-height:20px;color:#333}
.btn-more{left:292px;top:354px;width:171px;height:32px;border-radius:16px;background:linear-gradient(var(--teal-light),var(--teal));color:#fff;font-size:12px;text-align:center;line-height:32px;box-shadow:0 3px 4px rgba(0,0,0,.2)}
.hero-art{left:540px;top:88px;width:249px;height:318px;border-radius:46% 50% 20% 30%;background:radial-gradient(circle at 60% 35%,#4f86c4,#1f4a86 55%,rgba(20,50,100,0) 78%)}

/* location */
.sec-title{left:133px;top:433px;font-size:15.5px;font-weight:700;color:var(--heading);letter-spacing:.3px}
.sec-text{left:133px;top:462px;width:690px;font-size:10.5px;font-weight:300;line-height:20px;color:#333}
.field{background:var(--field);border:1px solid var(--field-border);font-size:11px;color:#a8a8a0;padding:12px 8px}
.addr-title{left:690px;top:545px;font-family:"Oswald",sans-serif;font-size:15px;color:#2a2a2a}
.addr-title span{color:var(--accent-red)}
.addr{left:718px;font-size:10.5px;font-style:italic;font-weight:400;line-height:17px;color:#222}
.icon{left:691px}

.map{left:128px;top:745px;width:719px;height:261px;border:2px solid #ddd;background:linear-gradient(135deg,#e9ece0,#f1efe8 50%,#e7e2cf)}
.zoom{left:727px;top:1005px;width:120px;height:22px;background:#111;color:#fff;font-size:9.5px;font-weight:500;display:flex;align-items:center;gap:6px;padding-left:8px}

.cta{top:1061px;width:225px;height:44px;background:#f7f7f1;border:1px solid #cfd0c5;padding:4px}
.cta-bar{position:absolute;left:10px;right:10px;top:9px;height:25px;font-size:11.5px;line-height:25px;color:#fff;white-space:nowrap;border-radius:2px}
.cta-pink{background:linear-gradient(#c76b9b,var(--pink));padding-left:38px}
.cta-pink em{font-style:italic}
.cta-pink span{font-weight:300}
.cta-blue{background:linear-gradient(#2b7aa6,var(--blue-btn));padding-left:66px;font-weight:500}
.phone-tab{left:637px;top:1054px;width:200px;height:66px}
.phone-num{left:697px;top:1095px;font-size:17px;color:#fff}
.phone-num b{font-weight:400;color:#9fdcd6}

footer{position:absolute;left:0;top:1119px;width:976px;height:81px;background:var(--footer);color:#fff;text-align:center}
.f-addr{position:absolute;left:0;right:0;top:12px;font-size:10.5px;font-style:italic;font-weight:300}
.f-mail{position:absolute;left:0;right:0;top:29px;font-size:10.5px;font-style:italic;color:#f3fbb8}
.f-line{position:absolute;left:135px;width:706px;top:46px;border-top:1px solid rgba(255,255,255,.5)}
.f-copy{position:absolute;left:0;right:0;top:56px;font-size:8.5px}
</style>
</head>
<body>

<div class="abs topband"></div>
<div class="abs navbar"></div>
<nav class="nav">
  <a style="left:124px">HOME</a><span class="dot" style="left:177px"></span>
  <a style="left:203px">SERVIÇOS</a><span class="dot" style="left:274px"></span>
  <a style="left:297px">INDICAÇÕES</a>
  <a style="left:597px">PERGUNTAS</a><span class="dot" style="left:671px"></span>
  <a style="left:689px">LOCALIZAÇÃO</a><span class="dot" style="left:777px"></span>
  <a style="left:790px">CONTATO</a>
</nav>
<div class="abs ribbon"></div>
<div class="abs logo"><span class="mark"></span><span class="name">Mente Lumo</span></div>

<section>
  <div class="abs hero"></div>
  <div class="abs hero-art" role="img" aria-label="Ilustração de cabeça humana em perfil com engrenagens no cérebro"></div>
  <div class="abs hero-kicker">O que é a</div>
  <h1 class="abs hero-title">Terapia Cognitiva?</h1>
  <p class="abs hero-text">A Terapia Cognitiva tem como método a interpretação de processos e conteúdos mentais (as cognições), e sua influência na vida cotidiana. O comportamento e a emoção vêm depois do processamento cognitivo. É vital conhecermos nossos pensamentos para termos controle sobre eles, e assim podemos: nutri-los, expandi-los, reduzi-los ou rejeitá-los.</p>
  <div class="abs btn-more">Leia Mais</div>
</section>

<section>
  <h2 class="abs sec-title">LOCALIZAÇÃO</h2>
  <p class="abs sec-text">Nos dias de hoje, todas as pessoas estão sujeitas a sofrer de algum disturbio psicológico. Isso acontece devido as pressões diárias que se não bem administradas, podem levar a diversas crises, afetando a vida pessoal, familiar e profissional. Realizo atendimentos para crianças, jovens, adultos, idosos e casais. Abaixo, você pode obter mais detalhes de algumas das mais comuns disfunções cogntivas:</p>

  <div class="abs field" style="left:140px;top:546px;width:251px;height:38px">Name</div>
  <div class="abs field" style="left:140px;top:607px;width:251px;height:38px">Email</div>
  <div class="abs field" style="left:140px;top:668px;width:251px;height:38px">Phone</div>
  <div class="abs field" style="left:414px;top:546px;width:252px;height:160px">Enquiry</div>

  <div class="abs addr-title">Address <span>Details</span></div>
  <svg class="abs icon" style="top:580px" width="16" height="16" viewBox="0 0 16 16"><path d="M2 1v15" stroke="#222" stroke-width="2"/><path d="M3 2h11l-3 3 3 3H3z" fill="#222"/></svg>
  <div class="abs addr" style="top:579px">Rua das Acácias, 158,<br>4º andar, Sala 12 - Centro -<br>Vila Serena, SP</div>
  <svg class="abs icon" style="top:643px" width="16" height="12" viewBox="0 0 16 12"><rect x="0.5" y="0.5" width="15" height="11" fill="#222"/><path d="M1 1l7 6 7-6" stroke="#fff" stroke-width="1.2" fill="none"/></svg>
  <div class="abs addr" style="top:639px">contato@mentelumo.net</div>
  <svg class="abs icon" style="top:675px" width="14" height="16" viewBox="0 0 14 16"><rect x="1" y="1" width="12" height="14" rx="2" fill="none" stroke="#222" stroke-width="2"/><rect x="4" y="11" width="6" height="2" fill="#222"/></svg>
  <div class="abs addr" style="top:674px">(11) 4050 - 7391</div>

  <div class="abs map" role="img" aria-label="Mapa de ruas mostrando a localização do consultório"></div>
  <div class="abs zoom"><svg width="12" height="12" viewBox="0 0 12 12"><circle cx="5" cy="5" r="3.5" stroke="#fff" stroke-width="1.6" fill="none"/><path d="M7.5 7.5l3.5 3.5" stroke="#fff" stroke-width="2"/></svg>Clique para ampliar</div>
</section>

<div class="abs cta" style="left:133px">
  <div class="cta-bar cta-pink">
    <svg style="position:absolute;left:3px;top:-4px" width="30" height="32" viewBox="0 0 30 32"><rect x="1" y="4" width="28" height="27" rx="2" fill="#fff" stroke="#999"/><rect x="1" y="4" width="28" height="8" fill="#c0392b"/><g fill="#bbb"><rect x="5" y="15" width="4" height="3"/><rect x="13" y="15" width="4" height="3"/><rect x="21" y="15" width="4" height="3"/><rect x="5" y="22" width="4" height="3"/><rect x="13" y="22" width="4" height="3"/><rect x="21" y="22" width="4" height="3"/></g></svg>
    <em>Agende online</em> <span>seu atendimento</span>
  </div>
</div>
<div class="abs cta" style="left:376px">
  <div class="cta-bar cta-blue">
    <svg style="position:absolute;left:4px;top:-6px" width="48" height="36" viewBox="0 0 48 36"><rect x="1" y="1" width="46" height="34" rx="3" fill="#333"/><rect x="4" y="4" width="40" height="28" fill="#8fc7a8"/><path d="M4 20l14-8 12 10 14-12" stroke="#e9d27a" stroke-width="3" fill="none"/><circle cx="14" cy="8" r="3" fill="#c0392b"/></svg>
    Veja onde estamos
  </div>
</div>

<svg class="abs phone-tab" viewBox="0 0 200 66" aria-hidden="true"><path d="M0 66L170 0l30 66z" fill="var(--teal)"/></svg>
<svg class="abs" style="left:668px;top:1090px" width="22" height="26" viewBox="0 0 22 26"><path d="M4 2l5 1 1 6-3 2c1 4 3 7 7 9l2-3 6 1 0 5c-1 2-4 3-7 2C8 22 3 15 2 7 2 4 3 2 4 2z" fill="#c0392b"/></svg>
<div class="abs phone-num"><b>(11)</b> 4050-7391</div>

<footer>
  <div class="f-addr">Rua das Acácias, 158, 4º andar, Sala 12 - Centro - Vila Serena, SP</div>
  <div class="f-mail">✉&nbsp; contato@mentelumo.net</div>
  <div class="f-line"></div>
  <div class="f-copy">Copyright ©2012 - Todos os direitos reservados</div>
</footer>

</body>
</html>
```